Property investment company needs a letterhead design!

We are a new residential and commercial property investment company. Name of the company is Morvessa Group, LLC. We have a new logo and now we need letterhead! We prefer to have a professional and upscale appearance. We don't have any fixed requirements, so be creative! Thank you for considering this project. We are so excited to see what happens!

Target Market(s)

Professional

Industry/Entity Type

Real Estate Development

```html
<!DOCTYPE html>
<html lang="en">
<head>
<meta charset="utf-8">
<title>Morvessa Group, LLC — Letterhead</title>
<link href="https://fonts.googleapis.com/css2?family=Poppins:wght@300;400;500;600&display=swap" rel="stylesheet">
<style>
  :root {
    --navy: #0f2240;
    --navy-soft: #1c355c;
    --sky: #1e9ad6;
    --ink: #2a2d33;
    --paper: #ffffff;
    --backdrop: #e9eaec;
  }
  * { margin: 0; padding: 0; box-sizing: border-box; }
  html, body {
    width: 1200px; height: 795px; overflow: hidden;
    background: var(--backdrop);
    font-family: "Poppins", sans-serif;
  }
  .letterhead {
    position: absolute; left: 338px; top: 27px;
    width: 523px; height: 740px;
    background: var(--paper);
    box-shadow: 0 6px 24px rgba(0,0,0,.12);
    overflow: hidden;
    color: var(--ink);
  }
  .brand {
    position: absolute; left: 48px; top: 48px;
    display: flex; align-items: center; gap: 8px;
    font-weight: 600; font-size: 15px; letter-spacing: .5px;
    color: var(--navy);
  }
  .brand-dot { width: 14px; height: 14px; border-radius: 50%; background: var(--navy); }
  .letter-date {
    position: absolute; right: 48px; top: 132px;
    font-size: 7.5px; font-weight: 300;
  }
  .letter-body {
    position: absolute; left: 48px; top: 168px; width: 427px;
    font-size: 8px; line-height: 1.55; font-weight: 300;
  }
  .salutation { font-weight: 600; font-size: 9px; margin-bottom: 8px; }
  .letter-body p { margin-bottom: 12px; }
  .closing { font-weight: 600; font-size: 8.5px; margin-top: 8px; }
  .signature-area {
    width: 110px; height: 36px; margin-top: 10px;
    background: linear-gradient(90deg, #eceef1, #f6f7f8);
  }
  .footer-art { position: absolute; left: 0; bottom: 0; width: 523px; height: 300px; }
  .footer-contact {
    position: absolute; left: 40px; bottom: 24px;
    color: #fff; font-size: 8px; font-weight: 300; line-height: 1.7;
  }
  .footer-contact li { list-style: none; display: flex; align-items: center; gap: 6px; }
  .footer-contact svg { width: 8px; height: 8px; fill: var(--sky); }
  .footer-divider {
    position: absolute; left: 218px; bottom: 26px;
    width: 1px; height: 40px; background: var(--sky);
  }
  .footer-address {
    position: absolute; left: 232px; bottom: 24px;
    color: #fff; font-size: 8px; font-weight: 300; line-height: 1.7;
  }
  .footer-address .company { color: var(--sky); font-weight: 400; }
</style>
</head>
<body>
<main class="letterhead">
  <div class="brand"><span class="brand-dot"></span>MORVESSA GROUP, LLC</div>

  <div class="letter-date">30 January 2080</div>

  <section class="letter-body">
    <div class="salutation">Dear Hallworth,</div>
    <p>Lorem ipsum dolor sit amet, consectetuer adipiscing elit, sed diam nonummy nibh euismod tincidunt ut laoreet dolore magna aliquam erat volutpat. Ut wisi enim ad minim veniam, quis nostrud exerci tation ullamcorper suscipit lobortis nisl ut aliquip ex ea commodo consequat. Duis dolore te feugait nulla facilisi. Nam liber tempor cum soluta nobis eleifend option congue nihil imperdiet doming id quod mazim placerat facer possim assum. Lorem ipsum dolor sit amet, doming id quod mazim placerat facer bouml. Consectetuer adipiscing elit, sed diam nonummy nibh euismod tincidunt ut laoreet doulore magna aliquam erat volutpat. Ut wisi enim ad minim erato.</p>
    <p>Consectetuer adipiscing elit, sed diam nonummy nibh euismod tincidunt utom laoreet dolore magna aliquam erat volutpat. Ut wisi enim ad minim veniam, quis nostrud exerci tation ullamcorper nisl suscipit lobortis nisl utiliomu aliquip ex ea commoduconsequat. Consectetuer adipiscing elit, sed diam nonummy nibh euismod tincidunt ut laoreet dolore magna aliquam erat volutpat wisi enica suscipit lobortis nisl utiliomu adipiscinei. Tation ullamcorper nisl suscipit lobortis nisl utiliomu aliquip ex ea commoduconsequat. Consectetuer adipiscing elit, sed diam nonummy nibh euismod tincidunt ut laoreet oni.</p>
    <div class="closing">Sincerely Yours</div>
    <div class="signature-area" role="img" aria-label="Handwritten signature"></div>
  </section>

  <svg class="footer-art" viewBox="0 0 523 300" preserveAspectRatio="none" aria-hidden="true">
    <polygon points="0,232 523,30 523,300 0,300" fill="var(--navy)"/>
    <polygon points="360,107 523,44 523,60 380,114" fill="var(--navy-soft)"/>
    <polygon points="430,50 523,14 523,20 440,52" fill="var(--sky)"/>
  </svg>

  <ul class="footer-contact">
    <li><svg viewBox="0 0 10 10"><path d="M2 0l2 2-1 1.5a6 6 0 003.5 3.5L8 6l2 2-1.5 2C4 10 0 6 0 1.5z"/></svg>(555) 218-4470</li>
    <li><svg viewBox="0 0 10 10"><path d="M0 2h10v6H0z M0 2l5 3.5L10 2" stroke="#0f2240" stroke-width=".8"/></svg>hello@morvessagroup.com</li>
    <li><svg viewBox="0 0 10 10"><circle cx="5" cy="5" r="5"/><path d="M0 5h10M5 0v10" stroke="#0f2240" stroke-width=".8"/></svg>www.morvessagroup.com</li>
  </ul>
  <div class="footer-divider"></div>
  <div class="footer-address">
    <div class="company">Morvessa Group, LLC</div>
    <div>418 N. Cedar Ave.</div>
    <div>Pine Hollow, MI 49001</div>
  </div>
</main>
</body>
</html>
```